Law Firm Business Cards/Letterhead/Envelopes
Holloway Law Firm, PLLC Business Cards/Letterhead/Envelopes
I need double sided standard sized Business Card [3.5" x 2"]
Selective use of Same font as logo and also may use other type of font
Simple
Martin J. Holloway
Attorney & Counselor at Law
2650 Prairie Ridge Road - Suite 1200
Bloomington, MN 55429
martin@holfirm.example
www.holfirm.example
The front of the card I would like to incorporate my logo and firm name, my name, title, address, numbers/fax, email and website. The business card WILL NOT have curved corners. Open to different possibilities but dont want the card too busy....I'd prefer something on the "simple" side...Same goes for envelope and letterhead.
Probably just Logo, Firm name and address all in upper left of envelope.
Letterhead - Logo and firm name up top somewhere...address at bottom....do not include my name and my title on letterhead.
The back of the card I would like to only incorporate the Logo and website OR Logo and firm name and website. The business card WILL NOT have curved corners. Possibly a different color back (possibly grey), but not necessarily. Possibly a watermark of the logo used somewhere...open to different possibilities but dont want the card too busy....I'd prefer something on the "simple" side...
Logo to the Left
Folder Template

```html
<!DOCTYPE html>
<html lang="en">
<head>
<meta charset="utf-8">
<title>Holloway Law Firm, PLLC — Business Card</title>
<link rel="stylesheet" href="https://fonts.googleapis.com/css2?family=Tinos:ital,wght@0,400;0,700;1,700&display=swap">
<style>
  :root {
    --backdrop: #e8e4dc;
    --navy-light: #3a6aa0;
    --navy-mid: #1f4677;
    --navy-dark: #0d2546;
    --silver: #b9bcc1;
    --card-white: #ffffff;
    --brand-blue: #1d4a7c;
    --ink-light: #ffffff;
  }
  html, body {
    margin: 0;
    padding: 0;
    width: 1200px;
    height: 965px;
    overflow: hidden;
    background: var(--backdrop);
  }
  .business-card {
    position: absolute;
    left: 100px;
    top: 196px;
    width: 1000px;
    height: 572px;
    overflow: hidden;
    background: var(--card-white);
    box-shadow: 0 6px 18px rgba(0,0,0,0.25);
    font-family: "Tinos", "Times New Roman", serif;
  }
  .card-shapes {
    position: absolute;
    inset: 0;
  }
  .contact-side {
    position: absolute;
    left: 47px;
    top: 0;
    color: var(--ink-light);
  }
  .attorney-name {
    position: absolute;
    top: 30px;
    margin: 0;
    font-size: 31px;
    font-weight: 700;
    white-space: nowrap;
  }
  .attorney-title {
    position: absolute;
    top: 72px;
    left: 4px;
    margin: 0;
    font-size: 22px;
    font-weight: 700;
    font-style: italic;
    white-space: nowrap;
  }
  .office-address {
    position: absolute;
    top: 296px;
    margin: 0;
    font-size: 22px;
    line-height: 27px;
    font-style: normal;
    white-space: nowrap;
  }
  .contact-list {
    position: absolute;
    top: 392px;
    margin: 0;
    padding: 0;
    list-style: none;
    font-size: 22px;
  }
  .contact-list li {
    display: flex;
    align-items: center;
    height: 40.5px;
    white-space: nowrap;
  }
  .contact-list svg {
    width: 22px;
    height: 22px;
    margin-right: 12px;
    fill: var(--ink-light);
  }
  .firm-identity {
    position: absolute;
    left: 570px;
    width: 420px;
    top: 0;
    height: 572px;
    display: flex;
    flex-direction: column;
    align-items: center;
    justify-content: center;
    gap: 18px;
  }
  .firm-mark {
    width: 52px;
    height: 52px;
    background: var(--brand-blue);
  }
  .firm-name {
    margin: 0;
    font-size: 34px;
    font-weight: 400;
    color: var(--brand-blue);
    white-space: nowrap;
  }
  .firm-website {
    margin: -6px 0 0;
    font-size: 20px;
    font-weight: 400;
    color: var(--brand-blue);
    white-space: nowrap;
  }
</style>
</head>
<body>
  <section class="business-card">
    <svg class="card-shapes" viewBox="0 0 1000 572" width="1000" height="572" aria-hidden="true">
      <defs>
        <radialGradient id="panel-glow" cx="0.38" cy="0.55" r="0.7">
          <stop offset="0" stop-color="#3a6aa0"/>
          <stop offset="0.55" stop-color="#1f4677"/>
          <stop offset="1" stop-color="#0d2546"/>
        </radialGradient>
      </defs>
      <path class="silver-band" d="M0 0 H628 C575 160 545 360 512 572 H0 Z" fill="#b9bcc1"/>
      <path class="navy-panel" d="M0 0 H602 C552 160 520 360 486 572 H0 Z" fill="url(#panel-glow)"/>
    </svg>

    <div class="contact-side">
      <h1 class="attorney-name">Martin J. Holloway</h1>
      <p class="attorney-title">Attorney &amp; Counselor at Law</p>
      <address class="office-address">2650 Prairie Ridge Road - Suite 1200<br>Bloomington, MN 55429</address>
      <ul class="contact-list">
        <li><svg viewBox="0 0 24 24"><path d="M6.6 10.8a15.1 15.1 0 0 0 6.6 6.6l2.2-2.2a1 1 0 0 1 1-.25 11.4 11.4 0 0 0 3.6.6 1 1 0 0 1 1 1V20a1 1 0 0 1-1 1A17 17 0 0 1 3 4a1 1 0 0 1 1-1h3.5a1 1 0 0 1 1 1 11.4 11.4 0 0 0 .6 3.6 1 1 0 0 1-.25 1z"/></svg>(1) (800) 555-0142</li>
        <li><svg viewBox="0 0 24 24"><path d="M6.6 10.8a15.1 15.1 0 0 0 6.6 6.6l2.2-2.2a1 1 0 0 1 1-.25 11.4 11.4 0 0 0 3.6.6 1 1 0 0 1 1 1V20a1 1 0 0 1-1 1A17 17 0 0 1 3 4a1 1 0 0 1 1-1h3.5a1 1 0 0 1 1 1 11.4 11.4 0 0 0 .6 3.6 1 1 0 0 1-.25 1z"/></svg>(952) 555-0187</li>
        <li><svg viewBox="0 0 24 24"><path d="M7 3h8v5H7z M4 9h16a1 1 0 0 1 1 1v8a1 1 0 0 1-1 1H4a1 1 0 0 1-1-1v-8a1 1 0 0 1 1-1z M7 14h10v6H7z"/></svg>(952) 555-0188</li>
        <li><svg viewBox="0 0 24 24"><path d="M12 2a10 10 0 1 0 5 18.7l-.9-1.7A8 8 0 1 1 20 12v1.2a1.8 1.8 0 0 1-3.6 0V7.5h-1.8v.9A4.6 4.6 0 1 0 15 15.6a3.6 3.6 0 0 0 6.8-2.4V12A10 10 0 0 0 12 2zm0 12.8a2.8 2.8 0 1 1 0-5.6 2.8 2.8 0 0 1 0 5.6z"/></svg>martin@holfirm.example</li>
      </ul>
    </div>

    <div class="firm-identity">
      <div class="firm-mark"></div>
      <p class="firm-name">Holloway Law Firm, PLLC</p>
      <p class="firm-website">www.holfirm.example</p>
    </div>
  </section>
</body>
</html>
```